I am a company selling interior designing materials

HI, I am selling interior design materials and require a namecard which is more outstanding while following a certain details placement as attached.

My clients are mainly interior designers so it has to attract their attention rather than feeling that its "just another namecard". I am selling wallcoverings, fabrics, acoustics and carpets.

Target Market(s)

interior designers designing hotels, commerical offices.

Contact Information for Business Card

As per attached.
Please change address to 47 Jalan 16 Tampines #05-02 Velmora Building Singapore 527314

Font styles to use
Other font styles liked:
• calibri

Requirements
Must have
• (1) company logo on top in the middle. Placement of contac details to be the same
• (2) company color is blue/green cymk 75/8/42/0
• (3) "KTV" logo to be prominent
• (4) You may change the logo but there should be a "swirl" surrounding the word KTV like current logo. The swirl pattern does not need to follow current logo and you may propose.
Should not have
• (1) there should not be any designs above "KTV" logo
• (2) no sharp triangles or angles

```html
<!DOCTYPE html>
<html lang="en">
<head>
<meta charset="utf-8">
<title>KaleVista Interior Furnishings – Business Card</title>
<link href="https://fonts.googleapis.com/css2?family=Lato:wght@400;700;900&display=swap" rel="stylesheet">
<style>
  :root{
    --teal:#23ada4;
    --charcoal:#3b3b3c;
    --ink:#2f3032;
    --paper:#ffffff;
    --backdrop:#ecebe8;
    --on-teal:#ffffff;
  }
  *{margin:0;padding:0;box-sizing:border-box}
  html,body{width:1200px;height:942px;overflow:hidden;background:var(--backdrop)}
  body{font-family:"Lato",Arial,sans-serif;position:relative}

  .card{position:absolute;width:545px;height:311px;border-radius:3px;box-shadow:0 6px 18px rgba(0,0,0,.18);overflow:hidden}
  .card--front{left:40px;top:316px;background:var(--paper)}
  .card--back{left:615px;top:316px;background:var(--teal)}

  /* front */
  .guide-line{position:absolute;left:58px;top:0;width:2px;height:270px;background:var(--teal)}
  .holder-name{position:absolute;left:96px;top:28px;font-size:28px;font-weight:700;color:var(--ink);letter-spacing:.3px}
  .holder-rule{position:absolute;left:96px;top:74px;width:36px;height:3px;background:var(--teal)}
  .contact{position:absolute;left:48px;display:flex;align-items:center;gap:14px;font-size:15px;color:var(--ink);white-space:nowrap}
  .contact svg{width:22px;height:22px;flex:none}
  .contact--mobile{top:102px}
  .contact--phone{top:136px}
  .contact--email{top:170px}

  .address-bar{position:absolute;left:78px;top:268px;width:444px;height:32px;background:var(--charcoal);color:var(--on-teal);font-size:13.5px;display:flex;align-items:center;padding-left:14px;letter-spacing:.2px;white-space:nowrap}
  .address-pin{position:absolute;left:42px;top:252px;width:36px;height:48px;background:var(--teal);display:flex;align-items:flex-start;justify-content:center;padding-top:8px}
  .address-pin svg{width:16px;height:20px}

  .lockup{position:absolute;display:flex;align-items:center;gap:12px}
  .lockup__text{display:flex;flex-direction:column}
  .lockup__name{font-weight:900;line-height:1;white-space:nowrap}
  .lockup__legal{text-transform:uppercase;font-weight:400;white-space:nowrap}
  .lockup__disc{border-radius:50%;flex:none}

  .card--front .lockup{right:26px;top:204px}
  .card--front .lockup__name{font-size:36px;color:var(--ink)}
  .card--front .lockup__legal{font-size:8.5px;color:var(--teal);margin-top:5px;letter-spacing:2.4px}
  .card--front .lockup__disc{width:52px;height:52px;border:5px solid var(--teal)}

  /* back */
  .card--back .lockup{left:50%;top:72px;transform:translateX(-50%)}
  .card--back .lockup__name{font-size:52px;color:var(--on-teal)}
  .card--back .lockup__legal{font-size:10px;color:var(--on-teal);margin-top:8px;letter-spacing:3.2px}
  .card--back .lockup__disc{width:74px;height:74px;border:7px solid var(--on-teal)}

  .services{position:absolute;left:0;right:0;bottom:46px;display:flex;justify-content:center;gap:16px;color:var(--on-teal);font-size:14px;letter-spacing:1px;text-transform:uppercase}
</style>
</head>
<body>

<section class="card card--front" aria-label="Business card front">
  <div class="guide-line"></div>
  <h1 class="holder-name">Lena Tay</h1>
  <div class="holder-rule"></div>

  <div class="contact contact--mobile">
    <svg viewBox="0 0 22 22" aria-hidden="true"><rect width="22" height="22" rx="3" fill="var(--teal)"/><rect x="7.5" y="4.5" width="7" height="13" rx="1.2" fill="none" stroke="#fff" stroke-width="1.6"/></svg>
    <span>(65) 9172 4410</span>
  </div>
  <div class="contact contact--phone">
    <svg viewBox="0 0 22 22" aria-hidden="true"><rect width="22" height="22" rx="3" fill="var(--teal)"/><path d="M7 5.5c1 0 1.5 2.6 1.5 2.6L7.6 9.4c.8 1.7 2 3 3.7 3.8l1.3-1s2.6.5 2.6 1.5v1.6c0 .6-.5 1-1 1C9 16.3 5.7 13 5.7 7c0-.5.4-1.5 1.3-1.5z" fill="#fff"/></svg>
    <span>(65) 6283 5176</span>
  </div>
  <div class="contact contact--email">
    <svg viewBox="0 0 22 22" aria-hidden="true"><rect width="22" height="22" rx="3" fill="var(--teal)"/><rect x="5" y="7" width="12" height="8.5" rx="1" fill="none" stroke="#fff" stroke-width="1.5"/><path d="M5.5 7.5 11 12l5.5-4.5" fill="none" stroke="#fff" stroke-width="1.5"/></svg>
    <span>lena@ktvfurnishings.com</span>
  </div>

  <div class="lockup">
    <div class="lockup__text">
      <span class="lockup__name">KaleVista</span>
      <span class="lockup__legal">Interior Furnishings Pte Ltd</span>
    </div>
    <span class="lockup__disc" aria-hidden="true"></span>
  </div>

  <div class="address-pin">
    <svg viewBox="0 0 16 20" aria-hidden="true"><path d="M8 1a6 6 0 0 0-6 6c0 4.5 6 12 6 12s6-7.5 6-12a6 6 0 0 0-6-6z" fill="#fff"/><circle cx="8" cy="7" r="2.2" fill="var(--teal)"/></svg>
  </div>
  <div class="address-bar">47 Jalan 16 Tampines #05-02 Velmora Building Singapore 527314</div>
</section>

<section class="card card--back" aria-label="Business card back">
  <div class="lockup">
    <div class="lockup__text">
      <span class="lockup__name">KaleVista</span>
      <span class="lockup__legal">Interior Furnishings Pte Ltd</span>
    </div>
    <span class="lockup__disc" aria-hidden="true"></span>
  </div>
  <p class="services">
    <span>Wallcoverings</span><span>|</span>
    <span>Acoustic</span><span>|</span>
    <span>Fabrics</span><span>|</span>
    <span>Carpet</span>
  </p>
</section>

</body>
</html>
```